Website design 5 pages + short Video + basic graphic optimization for a luxury Homestay - Resort website

I just need the website design for the main pages and optimised graphic images. The website will be mainly based on the following single-page scroll theme.

https://marquinstudio.com/demo/guesthouse-one-page/
FIGMA Templates https://marquinstudio.com/free-figma-design-files-for-hotel-and-vacation-rentals/
You can use these templates as a starting point but create something unique and luxurious.

Find all graphics files here :
1 https://www.storvanta.com/sc/k7q519wp4t2m8r5/AAHJ_Pwoxe47lu829Gbnczq3e
2 https://www.storvanta.com/sh/qmtrk61hxwedzpa/AAC8VolRUM5X7wGHP2NK4ejsu?dl=0

The following is the output :
1. Create website design ( Output high-quality PSD and JPEG files )
a. Homepage ( Example https://marquinstudio.com/demo/countryside2/ )
b. Blog ( Example https://marquinstudio.com/demo/countryside2/blog-2/ )
c. Packages ….. ( Example xxxxx )
d. Room ( Example https://marquinstudio.com/demo/guesthouse-one-page/accommodation/ravelo/ )
e. About us ( Example xxxxx )
f. Contact with embedded google maps ( Example https://marquinstudio.com/demo/hotelclassic/contact-2/ )

2. Short Video edit – 30 to 50 seconds

3. Optimise graphics for all pages and galleries ready to be used in the website ( Output high-quality JPEG files )

```html
<!DOCTYPE html>
<html lang="en">
<head>
<meta charset="utf-8">
<title>Ambra Vale — Countryside Eco House</title>
<link rel="stylesheet" href="https://fonts.googleapis.com/css2?family=Nunito+Sans:wght@400;600;700;800&family=Open+Sans:wght@400;600;700&family=Lora:wght@400;500&display=swap">
<style>
:root{
  --gold:#f7b538;
  --gold-soft:#fbc559;
  --band:#fcc14f;
  --ink:#1b1b1b;
  --dark:#1f1f1e;
  --darker:#161616;
  --text:#555;
  --white:#fff;
  --muted:#c9c9c9;
  --line:#e3e3e3;
  --serif:'Lora',serif;
  --head:'Nunito Sans',sans-serif;
  --body:'Open Sans',sans-serif;
}
*{margin:0;padding:0;box-sizing:border-box}
html,body{width:1200px;height:5187px;overflow:hidden}
body{font-family:var(--body);color:var(--ink);background:var(--white);position:relative}
section,header,footer{position:absolute;left:0;width:1200px;overflow:hidden}
.abs{position:absolute}
.photo{position:absolute;display:block}
.eyebrow{font-family:var(--serif);color:var(--gold);font-size:17px}
.h2{font-family:var(--head);font-weight:800;font-size:27px;line-height:36px}
.center{text-align:center;left:0;width:1200px}
.btn{position:absolute;display:flex;align-items:center;justify-content:center;font-family:var(--body);font-weight:700;font-size:10px}

/* header */
.site-header{top:0;height:60px;background:var(--dark)}
.brand{left:151px;top:18px;font-family:var(--head);font-weight:700;font-size:20px;color:var(--gold)}
.nav{font-family:var(--head);font-weight:700;font-size:11px;color:var(--white)}
.nav span{position:absolute;white-space:nowrap}
.social-dot{position:absolute;top:24px;width:12px;height:12px;border-radius:50%;background:var(--white)}
.book-top{left:972px;top:14px;width:93px;height:30px;background:var(--gold);color:var(--ink)}

/* hero */
.hero{top:60px;height:520px}
.hero .photo{inset:0;background:linear-gradient(180deg,#7fa6c9 0%,#a7bfd2 18%,#4f6e3a 45%,#2f4a22 75%,#1f3116 100%)}
.hero .shade{position:absolute;inset:0;background:rgba(0,0,0,.28)}
.hero-kicker{top:108px;font-family:var(--serif);color:var(--white);font-size:18px}
.hero-title{top:143px;font-family:var(--head);font-weight:800;font-size:44px;line-height:50px;color:var(--gold)}
.hero-text{top:258px;font-size:10px;line-height:19px;color:var(--white)}
.hero-book{left:521px;top:335px;width:105px;height:36px;background:var(--white);color:var(--ink)}
.play{position:absolute;border-radius:50%;background:var(--white)}

/* intro */
.intro{top:580px;height:477px;background:var(--white)}
.intro .ring{position:absolute;left:250px;top:70px;width:230px;height:330px;border-radius:50%;border:1px solid #f0f0f0}
.intro .eyebrow{left:135px;top:82px}
.intro .h2{left:135px;top:118px;width:340px;font-size:27px;line-height:36px;font-weight:700}
.intro p{position:absolute;left:135px;top:240px;width:355px;font-size:11px;line-height:19px;color:var(--text)}
.readmore{position:absolute;font-family:var(--head);font-weight:700;font-size:10px;color:var(--ink)}
.framed{border:6px solid var(--white);box-shadow:0 4px 16px rgba(0,0,0,.18)}

/* services */
.services{top:1057px;height:563px;background:linear-gradient(180deg,#2b231b,#1a1511 60%,#241c14)}
.services .eyebrow{top:70px}
.services .h2{top:100px;color:var(--white)}
.svc-card{position:absolute;top:171px;width:221px;height:296px;background:var(--white);text-align:center}
.svc-img{position:absolute;left:36px;top:18px;width:150px;height:150px;border-radius:50%;border:3px solid var(--gold);overflow:hidden}
.svc-img span{position:absolute;inset:6px;border-radius:50%}
.svc-card h3{position:absolute;top:184px;left:0;width:221px;font-family:var(--serif);font-weight:500;font-size:13px}
.svc-card p{position:absolute;top:208px;left:20px;width:181px;font-size:9.5px;line-height:19px;color:#777}
.svc-card .readmore{top:265px;left:0;width:221px;font-size:9.5px}
.arrow-btn{position:absolute;width:30px;height:30px;border-radius:50%;display:flex;align-items:center;justify-content:center}

/* call band */
.call-band{top:1620px;height:97px;background:var(--band)}
.call-band .eyebrow{left:135px;top:22px;color:var(--white)}
.call-band .need{position:absolute;left:135px;top:52px;font-family:var(--head);font-weight:800;font-size:20px;color:var(--ink)}
.call-number{position:absolute;left:570px;top:30px;font-family:var(--head);font-weight:800;font-size:27px;color:var(--white)}
.contact-btn{left:958px;top:33px;width:107px;height:36px;background:var(--darker);color:var(--white)}

/* amenities */
.amenities{top:1717px;height:668px;background:linear-gradient(90deg,#5c5f63,#7a7d80 45%,#5d6068)}
.amenities .shade{position:absolute;inset:0;background:rgba(20,20,20,.35)}
.amenities .eyebrow{left:131px;top:95px}
.amenities .h2{left:131px;top:128px;width:330px;color:var(--white);font-size:27px;line-height:36px}
.amenities .lead{position:absolute;left:131px;top:255px;width:360px;font-size:10px;line-height:20px;color:var(--white)}
.feat{position:absolute;left:131px;width:360px;color:var(--white)}
.feat b{position:absolute;left:54px;top:0;font-size:8.5px;font-weight:700}
.feat span{position:absolute;left:54px;top:17px;width:300px;font-size:10px;line-height:19px}
.feat svg{position:absolute;left:0;top:-2px}
.divider{position:absolute;left:183px;width:306px;height:1px;background:rgba(255,255,255,.35)}

/* farmhouse */
.farm{top:2385px;height:343px;background:linear-gradient(180deg,#2c3b24,#3e5631 50%,#1f2b18)}
.farm .shade{position:absolute;inset:0;background:rgba(0,0,0,.35)}
.farm .eyebrow{top:92px}
.farm .h2{top:127px;color:var(--white);font-size:24px}

/* gallery */
.garden{top:2728px;height:638px;background:linear-gradient(180deg,#1f241a,#2a3220 50%,#181c14)}
.garden .shade{position:absolute;inset:0;background:rgba(0,0,0,.35)}
.garden .eyebrow{top:86px}
.garden .h2{top:124px;color:var(--white);font-size:26px}
.dots{position:absolute;display:flex;gap:5px}
.dots i{width:6px;height:6px;border-radius:50%;background:#bbb;display:block}
.dots i.on{background:var(--gold)}

/* booking */
.booking{top:3366px;height:411px;background:#1b1b1b}
.booking .eyebrow{left:642px;top:70px}
.booking .h2{left:642px;top:105px;color:var(--white);font-size:27px}
.booking p{position:absolute;left:642px;top:151px;width:340px;font-size:9.5px;line-height:20px;color:var(--muted)}
.field{position:absolute;left:642px;width:334px;height:30px;border:1px solid #666;background:#222;color:#bbb;font-size:9px;padding:9px 12px}
.field svg{position:absolute;right:10px;top:8px}
.avail-btn{left:642px;top:318px;width:334px;height:36px;background:var(--white);color:var(--ink)}

/* rooms */
.rooms{top:3777px;height:776px;background:linear-gradient(180deg,#1a1816,#2b241c 40%,#1c1916)}
.rooms .shade{position:absolute;inset:0;background:rgba(0,0,0,.25)}
.rooms .eyebrow{top:92px}
.rooms .h2{top:133px;color:var(--white);font-size:26px}
.room{position:absolute;top:233px;width:300px;height:440px}
.room .photo{left:0;top:0;width:300px;height:288px}
.tag{position:absolute;left:20px;top:20px;height:22px;padding:0 12px;background:var(--gold);font-size:8px;font-weight:700;display:flex;align-items:center}
.price{position:absolute;right:0;top:242px;width:82px;height:46px;background:var(--white);text-align:center;font-size:9px;font-weight:700;padding-top:10px;line-height:13px}
.price small{display:block;font-size:7.5px;font-weight:600}
.room h4{position:absolute;top:305px;left:0;font-family:var(--head);font-size:11px;font-weight:800;color:var(--white)}
.room p{position:absolute;top:326px;left:0;width:280px;font-size:9.5px;line-height:18px;color:var(--muted)}
.room .btn{top:412px;left:0;width:106px;height:26px;font-size:8px}
.slide-arrow{position:absolute;top:135px}

/* testimonials */
.testimonials{top:4553px;height:304px;background:linear-gradient(180deg,#2a251f,#1d1a17)}
.testimonials .shade{position:absolute;inset:0;background:rgba(0,0,0,.2)}
.testimonials .eyebrow{left:131px;top:55px}
.testimonials .h2{left:131px;top:95px;color:var(--white);font-size:26px}
.quote{position:absolute;top:32px;width:264px;height:210px;background:var(--white);text-align:center}
.avatar{position:absolute;top:-26px;left:110px;width:44px;height:44px;border-radius:50%;background:linear-gradient(180deg,#d2c6b8,#8c7a68);border:3px solid var(--white)}
.stars{position:absolute;top:26px;left:0;width:264px;display:flex;justify-content:center;gap:2px}
.quote h5{position:absolute;top:44px;left:0;width:264px;font-size:10px;font-weight:700}
.quote .role{position:absolute;top:60px;left:0;width:264px;font-size:8px;color:var(--gold)}
.quote p{position:absolute;top:80px;left:22px;width:220px;font-size:9.5px;line-height:19px;color:#777}
.qmark{position:absolute;top:158px;left:112px;font-family:var(--serif);font-size:60px;color:#e6e6e6;line-height:1}

/* footer */
.site-footer{top:4857px;height:330px;background:#262626}
.foot-brand{left:144px;top:80px;font-family:var(--head);font-weight:700;font-size:19px;color:var(--gold)}
.foot-text{position:absolute;left:133px;top:126px;width:230px;font-size:9.5px;line-height:18px;color:var(--muted)}
.foot-soc{position:absolute;top:193px;width:20px;height:20px;background:var(--gold)}
.foot-col{position:absolute;top:75px;color:var(--white)}
.foot-col h6{font-family:var(--head);font-weight:700;font-size:13px;color:var(--gold);margin-bottom:16px}
.foot-col li{list-style:none;font-size:9.5px;height:35.5px}
.contact-row{position:absolute;left:783px;display:flex;align-items:center;gap:12px;font-size:9.5px;color:var(--white)}
.contact-row i{width:20px;height:20px;border-radius:50%;background:var(--gold);display:flex;align-items:center;justify-content:center}
.copyright{position:absolute;left:0;top:300px;width:1200px;height:30px;background:#1c1c1c;color:var(--muted);font-size:9px;text-align:center;line-height:30px}
</style>
</head>
<body>

<header class="site-header">
  <div class="abs brand">Ambra Vale</div>
  <nav class="abs nav" style="left:0;top:23px;">
    <span style="left:461px;color:var(--gold)">Home</span>
    <span style="left:517px">Pages</span>
    <span style="left:574px">Features</span>
    <span style="left:646px">Blog</span>
    <span style="left:697px">Contact</span>
  </nav>
  <i class="social-dot" style="left:870px"></i>
  <i class="social-dot" style="left:902px"></i>
  <i class="social-dot" style="left:934px"></i>
  <div class="btn book-top">Book Now</div>
</header>

<section class="hero">
  <div class="photo" role="img" aria-label="Green A-frame guest house among pine forest under a blue sky"></div>
  <div class="shade"></div>
  <div class="abs center hero-kicker">The perfect place to escape</div>
  <h1 class="abs center hero-title">Experience something new<br>every moment</h1>
  <p class="abs center hero-text">Welcome to our countryside vacation rental! Our property is the perfect place to escape<br>the hustle and bustle of city life and enjoy a relaxing and peaceful vacation.</p>
  <div class="btn hero-book">Book Now</div>
  <div class="play" style="left:642px;top:335px;width:36px;height:36px">
    <svg width="36" height="36"><circle cx="18" cy="18" r="12" fill="var(--gold)"/><path d="M15 13 L23 18 L15 23Z" fill="#fff"/></svg>
  </div>
</section>

<section class="intro">
  <div class="ring"></div>
  <div class="eyebrow abs">Escape The City</div>
  <h2 class="h2 abs">Welcome to the quiet<br>eco house. enjoy and get<br>inspired.</h2>
  <p>Our spacious and comfortable home is perfect for large groups, and we have plenty of outdoor space for kids to run and play. we also have a private pool and hot tub, perfect for relaxing after a long day of hiking or exploring the local area.</p>
  <div class="readmore" style="left:135px;top:348px">Read More &rarr;</div>
  <div class="photo framed" style="left:687px;top:60px;width:376px;height:352px;background:linear-gradient(160deg,#2a2a2a,#6b4a1c 45%,#d69a3a 60%,#1c1c1c)" role="img" aria-label="Wooden A-frame cabin lit warmly at night"></div>
  <div class="photo framed" style="left:548px;top:112px;width:267px;height:161px;background:linear-gradient(180deg,#9ec0e0,#4e8a45 50%,#2f5a2a)" role="img" aria-label="Teal-roofed cottage on a green hillside"></div>
  <div class="photo framed" style="left:648px;top:221px;width:324px;height:181px;background:linear-gradient(180deg,#a8c6e0,#5f8f4a 45%,#3c6a2e)" role="img" aria-label="Cottage seen from above among trees"></div>
</section>

<section class="services">
  <div class="eyebrow abs center">Your Services</div>
  <h2 class="h2 abs center">At Your Service</h2>
  <div class="arrow-btn" style="left:82px;top:303px;background:var(--white)"><svg width="12" height="12"><path d="M9 6H3M5 3L2 6L5 9" stroke="#222" stroke-width="1.5" fill="none"/></svg></div>
  <div class="arrow-btn" style="left:1084px;top:303px;background:var(--white)"><svg width="12" height="12"><path d="M3 6H9M7 3L10 6L7 9" stroke="#222" stroke-width="1.5" fill="none"/></svg></div>

  <div class="svc-card" style="left:133px">
    <div class="svc-img"><span style="background:linear-gradient(135deg,#e07a2f,#8a4b22)" role="img" aria-label="Row of laundry washing machines"></span></div>
    <h3>Laundry Service</h3>
    <p>There Are Laundry Facilities And Kitchen Facilities For Guests To Use.</p>
    <div class="readmore">Read More &nbsp;&rarr;</div>
  </div>
  <div class="svc-card" style="left:370px">
    <div class="svc-img"><span style="background:linear-gradient(135deg,#e8d8c0,#b5804a)" role="img" aria-label="Breakfast table with plates of food"></span></div>
    <h3>Breakfast Service</h3>
    <p>The hostel offers a free breakfast every morning</p>
    <div class="readmore">Read More &nbsp;&rarr;</div>
  </div>
  <div class="svc-card" style="left:608px">
    <div class="svc-img"><span style="background:linear-gradient(135deg,#cfd6dc,#7a6a4a)" role="img" aria-label="Glasses of beer being raised"></span></div>
    <h3>Local C And Wines</h3>
    <p>There is also a bar on-site that serves local beers and wines</p>
    <div class="readmore">Read More &nbsp;&rarr;</div>
  </div>
  <div class="svc-card" style="left:845px">
    <div class="svc-img"><span style="background:linear-gradient(180deg,#dfe7ee,#f0a52a 55%,#c9cfd4)" role="img" aria-label="Orange shuttle van"></span></div>
    <h3>Shuttle Service</h3>
    <p>Avoid the hassle and take advantage of our complimentary</p>
    <div class="readmore">Read More &nbsp;&rarr;</div>
  </div>
</section>

<section class="call-band">
  <div class="eyebrow abs">24/7 Callcenter</div>
  <div class="need">Need Any Services ?</div>
  <svg class="abs" style="left:518px;top:32px" width="40" height="34" viewBox="0 0 40 34"><path d="M8 4c-3 1-5 4-4 8 2 8 9 15 17 17 4 1 7-1 8-4l-5-5-4 2c-4-2-7-5-9-9l2-4z" fill="none" stroke="#222" stroke-width="2"/><path d="M22 6a8 8 0 0 1 8 8M22 1a13 13 0 0 1 13 13" fill="none" stroke="#222" stroke-width="2"/></svg>
  <div class="call-number">0-800-640-0-210</div>
  <div class="btn contact-btn">Contact Us</div>
</section>

<section class="amenities">
  <div class="shade"></div>
  <div class="eyebrow abs">Amenities &amp; Benefits</div>
  <h2 class="h2 abs">Surrounded By Nature, Stunning Views Of The Countryside.</h2>
  <p class="lead">Country rentals often come with extra amenities, such as pools, tennis courts, and hiking trails. this can be a great way to enjoy your vacation without having to leave the property.</p>
  <div class="feat" style="top:365px">
    <svg width="32" height="28" viewBox="0 0 32 28"><path d="M3 14 16 3l13 11M7 11v14h18V11" fill="var(--gold)" stroke="var(--gold)" stroke-width="2"/></svg>
    <b>Entire Home</b><span>You'll Have The Tiny House To Yourself.</span>
  </div>
  <div class="divider" style="top:415px"></div>
  <div class="feat" style="top:440px">
    <svg width="32" height="30" viewBox="0 0 32 30"><path d="M20 2 12 18M4 28l4-12h10l4 12z" fill="var(--gold)" stroke="var(--gold)" stroke-width="2"/></svg>
    <b>Enhanced Clean</b><span>This Host Committed To Staybrook's 5-Step Enhanced Cleaning Process</span>
  </div>
  <div class="divider" style="top:511px"></div>
  <div class="feat" style="top:537px">
    <svg width="32" height="30" viewBox="0 0 32 30"><path d="M16 2 5 6v8c0 7 5 12 11 14 6-2 11-7 11-14V6z" fill="var(--gold)"/><path d="M11 15l4 4 7-8" stroke="#fff" stroke-width="2" fill="none"/></svg>
    <b>Self Check-In</b><span>Check Yourself In With The Lockbox.</span>
  </div>
  <div class="photo" style="left:556px;top:68px;width:398px;height:510px;background:linear-gradient(180deg,#4d7d3a,#6a9a4a 35%,#3f6a30 60%,#6b6250 100%)" role="img" aria-label="Stone path leading through trees to the teal-roofed cottage"></div>
  <div class="photo" style="left:866px;top:286px;width:205px;height:264px;border:6px solid var(--white);background:linear-gradient(180deg,#79a858,#2f8a74 45%,#4a7a30)" role="img" aria-label="Teal A-frame cottage surrounded by greenery"></div>
</section>

<section class="farm">
  <div class="photo" style="inset:0" role="img" aria-label="Teal roof in the foreground with terraced hills behind"></div>
  <div class="shade"></div>
  <div class="eyebrow abs center">A Charming Farmhouse</div>
  <h2 class="h2 abs center">Looking For A Relaxing Country<br>Vacation Rental?</h2>
  <div class="play" style="left:578px;top:222px;width:44px;height:44px">
    <svg width="44" height="44"><path d="M18 15 L29 22 L18 29Z" fill="var(--gold)"/></svg>
  </div>
</section>

<section class="garden">
  <div class="shade"></div>
  <div class="eyebrow abs center">About Countryside</div>
  <h2 class="h2 abs center">A Secret Garden In The Countryside</h2>
  <div class="photo" style="left:95px;top:201px;width:241px;height:222px;background:linear-gradient(180deg,#8ab3de,#cfe0ef 30%,#4d7a3a 60%,#2f4d25)" role="img" aria-label="Tall pines against a bright sky"></div>
  <div class="photo" style="left:352px;top:246px;width:242px;height:277px;background:linear-gradient(180deg,#5c8ec8,#a9c6e2 30%,#5f8a45 60%,#3d5a2d)" role="img" aria-label="Guests walking across a grassy meadow"></div>
  <div class="photo" style="left:608px;top:201px;width:242px;height:222px;background:linear-gradient(180deg,#6f9a4c,#4a7a34 50%,#2f5324)" role="img" aria-label="Dense garden foliage"></div>
  <div class="photo" style="left:866px;top:246px;width:241px;height:277px;background:linear-gradient(180deg,#3f78c4,#7eb0df 30%,#3a8f73 55%,#3f6e2c)" role="img" aria-label="Teal A-frame cottage under a blue sky"></div>
  <div class="arrow-btn" style="left:78px;top:323px;background:var(--gold)"><svg width="12" height="12"><path d="M8 2L4 6L8 10" stroke="#fff" stroke-width="1.5" fill="none"/></svg></div>
  <div class="arrow-btn" style="left:1088px;top:369px;background:var(--gold)"><svg width="12" height="12"><path d="M4 2L8 6L4 10" stroke="#fff" stroke-width="1.5" fill="none"/></svg></div>
  <div class="dots" style="left:574px;top:556px"><i class="on"></i><i></i><i></i><i></i></div>
</section>

<section class="booking">
  <div class="photo" style="left:0;top:0;width:562px;height:411px;background:linear-gradient(160deg,#5a8a3a,#1f9a86 40%,#2a7a6a 60%,#6a8a3a 85%,#b08a3a)" role="img" aria-label="Teal A-frame roof framed by grass and foliage"></div>
  <svg class="abs" style="left:1060px;top:235px" width="120" height="110" viewBox="0 0 120 110"><path d="M10 55 60 12l50 43M25 45v55h70V45M50 100V70h20v30" stroke="#2e2e2e" stroke-width="3" fill="none"/></svg>
  <div class="eyebrow abs">Booking</div>
  <h2 class="h2 abs">Book Today</h2>
  <p>This house is one of the favorite houses of our clients, so they talk about it and leave reviews.</p>
  <div class="field" style="top:211px">Check-In Date<svg width="12" height="12"><rect x="1" y="2" width="10" height="9" fill="none" stroke="#bbb"/><path d="M1 5h10" stroke="#bbb"/></svg></div>
  <div class="field" style="top:261px">Check-Out Date<svg width="12" height="12"><rect x="1" y="2" width="10" height="9" fill="none" stroke="#bbb"/><path d="M1 5h10" stroke="#bbb"/></svg></div>
  <div class="btn avail-btn">Check Availability</div>
</section>

<section class="rooms">
  <div class="shade"></div>
  <div class="eyebrow abs center">Amazing Views!</div>
  <h2 class="h2 abs center">Equipped With All The Necessary<br>Amenities</h2>

  <div class="room" style="left:131px">
    <div class="photo" style="background:linear-gradient(180deg,#7fa3c7,#6e9a4a 30%,#4a7a34 65%,#2f5a2a)" role="img" aria-label="Terraced green hills seen from a porch"></div>
    <div class="tag">Private Porch</div>
    <svg class="slide-arrow" style="left:14px" width="10" height="14"><path d="M8 1 2 7l6 6" stroke="#fff" stroke-width="2" fill="none"/></svg>
    <svg class="slide-arrow" style="left:276px" width="10" height="14"><path d="M2 1l6 6-6 6" stroke="#fff" stroke-width="2" fill="none"/></svg>
    <div class="price">$399<small>/Night</small></div>
    <h4>THE COTTAGE</h4>
    <p>This room is located in a cottage on the water. It has a king sized bed, a whirlpool tub, and a private porch.</p>
    <div class="btn" style="background:var(--white);color:var(--ink)">Check Availability</div>
  </div>
  <div class="room" style="left:447px">
    <div class="photo" style="background:linear-gradient(180deg,#6f98c8,#4a8a6a 40%,#3f6e2c 70%,#2f4d22)" role="img" aria-label="Farmhouse with teal roof among trees"></div>
    <div class="tag">Private Porch</div>
    <svg class="slide-arrow" style="left:14px" width="10" height="14"><path d="M8 1 2 7l6 6" stroke="#fff" stroke-width="2" fill="none"/></svg>
    <svg class="slide-arrow" style="left:276px" width="10" height="14"><path d="M2 1l6 6-6 6" stroke="#fff" stroke-width="2" fill="none"/></svg>
    <div class="price">$399<small>/Night</small></div>
    <h4>THE FARMHOUSE</h4>
    <p>This room is located in a cottage on the water. It has a king sized bed, a whirlpool tub, and a private porch.</p>
    <div class="btn" style="background:var(--gold);color:var(--ink)">Check Availability</div>
  </div>
  <div class="room" style="left:763px">
    <div class="photo" style="background:linear-gradient(180deg,#8bb06a,#5a8a3a 40%,#3a6a2a 70%,#2a4a1e)" role="img" aria-label="Cabin hidden in lush forest"></div>
    <div class="tag">Private Porch</div>
    <svg class="slide-arrow" style="left:14px" width="10" height="14"><path d="M8 1 2 7l6 6" stroke="#fff" stroke-width="2" fill="none"/></svg>
    <svg class="slide-arrow" style="left:276px" width="10" height="14"><path d="M2 1l6 6-6 6" stroke="#fff" stroke-width="2" fill="none"/></svg>
    <div class="price">$399<small>/Night</small></div>
    <h4>THE CABIN</h4>
    <p>This room is located in a cottage on the water. It has a king sized bed, a whirlpool tub, and a private porch.</p>
    <div class="btn" style="background:var(--white);color:var(--ink)">Check Availability</div>
  </div>
</section>

<section class="testimonials">
  <div class="shade"></div>
  <div class="eyebrow abs">Testimonial</div>
  <h2 class="h2 abs">A Few Words From<br>Our Happy Clients</h2>

  <div class="quote" style="left:439px">
    <div class="avatar" role="img" aria-label="Guest portrait"></div>
    <div class="stars"><svg width="60" height="10"><g fill="var(--gold)"><path d="M5 0l1.5 3.2 3.5.4-2.6 2.4.7 3.5L5 7.8 1.9 9.5l.7-3.5L0 3.6l3.5-.4z"/><path transform="translate(12)" d="M5 0l1.5 3.2 3.5.4-2.6 2.4.7 3.5L5 7.8 1.9 9.5l.7-3.5L0 3.6l3.5-.4z"/><path transform="translate(24)" d="M5 0l1.5 3.2 3.5.4-2.6 2.4.7 3.5L5 7.8 1.9 9.5l.7-3.5L0 3.6l3.5-.4z"/><path transform="translate(36)" d="M5 0l1.5 3.2 3.5.4-2.6 2.4.7 3.5L5 7.8 1.9 9.5l.7-3.5L0 3.6l3.5-.4z"/><path transform="translate(48)" d="M5 0l1.5 3.2 3.5.4-2.6 2.4.7 3.5L5 7.8 1.9 9.5l.7-3.5L0 3.6l3.5-.4z"/></g></svg></div>
    <h5>Clara Denholm</h5><div class="role">Adventurer</div>
    <p>"When you are designing with Lorem Ipsum you diminish the importance of the copy by lowering it to the same level as any other visual element.</p>
    <div class="qmark">&rdquo;</div>
  </div>
  <div class="quote" style="left:723px">
    <div class="avatar" role="img" aria-label="Guest portrait"></div>
    <div class="stars"><svg width="60" height="10"><g fill="var(--gold)"><path d="M5 0l1.5 3.2 3.5.4-2.6 2.4.7 3.5L5 7.8 1.9 9.5l.7-3.5L0 3.6l3.5-.4z"/><path transform="translate(12)" d="M5 0l1.5 3.2 3.5.4-2.6 2.4.7 3.5L5 7.8 1.9 9.5l.7-3.5L0 3.6l3.5-.4z"/><path transform="translate(24)" d="M5 0l1.5 3.2 3.5.4-2.6 2.4.7 3.5L5 7.8 1.9 9.5l.7-3.5L0 3.6l3.5-.4z"/><path transform="translate(36)" d="M5 0l1.5 3.2 3.5.4-2.6 2.4.7 3.5L5 7.8 1.9 9.5l.7-3.5L0 3.6l3.5-.4z"/><path transform="translate(48)" d="M5 0l1.5 3.2 3.5.4-2.6 2.4.7 3.5L5 7.8 1.9 9.5l.7-3.5L0 3.6l3.5-.4z"/></g></svg></div>
    <h5>Clara Denholm</h5><div class="role">Adventurer</div>
    <p>"When you are designing with Lorem Ipsum you diminish the importance of the copy by lowering it to the same level as any other visual element.</p>
    <div class="qmark">&rdquo;</div>
  </div>
  <div class="quote" style="left:1007px">
    <div class="avatar" role="img" aria-label="Guest portrait"></div>
    <div class="stars"><svg width="60" height="10"><g fill="var(--gold)"><path d="M5 0l1.5 3.2 3.5.4-2.6 2.4.7 3.5L5 7.8 1.9 9.5l.7-3.5L0 3.6l3.5-.4z"/><path transform="translate(12)" d="M5 0l1.5 3.2 3.5.4-2.6 2.4.7 3.5L5 7.8 1.9 9.5l.7-3.5L0 3.6l3.5-.4z"/><path transform="translate(24)" d="M5 0l1.5 3.2 3.5.4-2.6 2.4.7 3.5L5 7.8 1.9 9.5l.7-3.5L0 3.6l3.5-.4z"/><path transform="translate(36)" d="M5 0l1.5 3.2 3.5.4-2.6 2.4.7 3.5L5 7.8 1.9 9.5l.7-3.5L0 3.6l3.5-.4z"/><path transform="translate(48)" d="M5 0l1.5 3.2 3.5.4-2.6 2.4.7 3.5L5 7.8 1.9 9.5l.7-3.5L0 3.6l3.5-.4z"/></g></svg></div>
    <h5>Clara Denholm</h5><div class="role">Adventurer</div>
    <p>"When you are designing with Lorem Ipsum you diminish the importance of the copy by lowering it to the same level as any other visual element.</p>
    <div class="qmark">&rdquo;</div>
  </div>
  <div class="dots" style="left:835px;top:233px"><i class="on"></i><i></i><i></i><i></i></div>
</section>

<footer class="site-footer">
  <div class="abs foot-brand">Ambra Vale</div>
  <p class="foot-text">When you are designing with Lorem Ipsum you diminish the importance of the copy by lowering it to the same level</p>
  <i class="foot-soc" style="left:133px"></i>
  <i class="foot-soc" style="left:165px"></i>
  <i class="foot-soc" style="left:197px"></i>
  <i class="foot-soc" style="left:229px"></i>
  <ul class="foot-col" style="left:451px"><h6>Explore</h6><li>Home</li><li>About</li><li>Services</li><li>Blog</li></ul>
  <ul class="foot-col" style="left:596px"><h6>Quick link</h6><li>Our Place</li><li>Our Menu</li><li>Why Us</li><li>Room Styles</li></ul>
  <div class="foot-col" style="left:783px"><h6>Contact us</h6></div>
  <div class="contact-row" style="top:100px"><i><svg width="10" height="8"><rect x=".5" y=".5" width="9" height="7" fill="none" stroke="#fff"/><path d="M.5 .5 5 4l4.5-3.5" stroke="#fff" fill="none"/></svg></i>info@ambravale.com</div>
  <div class="contact-row" style="top:135px"><i><svg width="10" height="10"><path d="M2 1c-1 1-1 3 1 5s4 3 6 2l-2-2-1 1C5 6 4 5 3 4l1-1z" fill="#fff"/></svg></i>1-800-314-7720</div>
  <div class="contact-row" style="top:170px"><i><svg width="10" height="12"><path d="M5 11S1 7 1 4.5a4 4 0 0 1 8 0C9 7 5 11 5 11z" fill="#fff"/><circle cx="5" cy="4.5" r="1.4" fill="var(--gold)"/></svg></i>Lindenholt, Vale County, 48210</div>
  <div class="copyright">Copyright. All right reserved.</div>
</footer>

</body>
</html>
```